Redesign of my Homepage - Online resource for anyone to learn American Sign Language

I would like to have a new homepage design http://www.HandwiseLessons.example . My business is a website for anyone to learn American Sign Language. There are over 300 video lessons, with each lesson having 20 vocabulary words, retention exercises, 16,000 video dictionary etc. It is a very extensive site. It is a self paced website. If you need a log in to see what customers see, please let me know. I would like to keep the same color scheme. I want the website to look modern and clean. I want a fresh look! I want something that is easy to navigate, attracts customers, and easy to follow. I would like the final design to communicate that my website is for anyone to learn how to sign with this incredible program.

Target Market(s)

Students taking American Sign Language, Parents with Deaf children, future interpreters for the deaf, co-workers of the Deaf. Also, schools that offer American Sign Language (online schools, homeschools, etc. ).

Industry/Entity Type

Business

Number of Pages Required

1 page

Requirements
Must have
• My project must be very clean and clear. I want my homepage to show that this is a program for people to learn how American Sign Language.
Nice to have
• Not sure. Surprise me.

```html
<!DOCTYPE html>
<html lang="en">
<head>
<meta charset="utf-8">
<title>Handwise Lessons – Learn American Sign Language Online</title>
<link href="https://fonts.googleapis.com/css2?family=Mulish:wght@400;500;600&family=Asap+Condensed:wght@400;500&display=swap" rel="stylesheet">
<style>
:root{
  --black:#0b0b0b;
  --white:#ffffff;
  --green:#19c63b;
  --ink:#1a1a1a;
  --body:#444444;
  --muted:#6b6b6b;
  --field:#c9c9c9;
  --soft:#f3f3f3;
}
*{margin:0;padding:0;box-sizing:border-box}
html,body{width:754px;height:1200px;overflow:hidden;background:var(--white)}
body{font-family:"Mulish",sans-serif;color:var(--ink)}
.page{position:relative;width:754px;height:1200px;overflow:hidden}

.topbar{position:absolute;left:0;top:0;width:754px;height:24px;background:var(--black);color:var(--white);font-size:7.5px}
.topbar .contact{position:absolute;left:70px;top:7px;display:flex;gap:16px;align-items:center}
.topbar .contact span{display:flex;align-items:center;gap:6px}
.topbar .social{position:absolute;right:70px;top:8px;display:flex;gap:8px}
.topbar .social i{display:block;width:8px;height:8px;background:var(--white);border-radius:1px}

.header{position:absolute;left:0;top:24px;width:754px;height:106px;border-bottom:1px solid var(--black)}
.brand{position:absolute;left:70px;top:40px;display:flex;align-items:center;gap:8px}
.brand .mark{width:20px;height:20px;border-radius:50%;background:var(--green)}
.brand .name{font-size:19px;font-weight:600;color:var(--ink);line-height:1}
.tagline{position:absolute;right:70px;top:12px;font-size:10.5px;font-weight:600}
.login{position:absolute;right:70px;top:31px;width:129px}
.login .field{height:16px;border:1px solid var(--field);font-size:6.5px;color:#a8a8a8;padding:4px 7px;margin-bottom:5px}
.login .actions{display:flex;justify-content:flex-end;align-items:center;gap:13px;margin-top:6px}
.login .forgot{font-size:7px;color:var(--ink)}
.login .signin{background:var(--black);color:var(--white);font-size:8px;padding:3px 10px}

.nav{position:absolute;left:75px;top:130px;height:30px;display:flex;gap:23px;font-size:9.5px;font-weight:500}
.nav a{color:var(--ink);text-decoration:none;padding-top:10px;position:relative}
.nav a.active::before{content:"";position:absolute;left:-5px;right:-5px;top:0;height:2px;background:var(--green)}

.hero{position:absolute;left:0;top:160px;width:754px;height:284px}
.hero .photo{position:absolute;inset:0;background:linear-gradient(180deg,#8d8478 0%,#6e5f52 45%,#4e4036 100%)}
.hero .lead{position:absolute;left:92px;top:76px;width:570px;font-family:"Asap Condensed",sans-serif;font-size:17.5px;line-height:26px;color:var(--white);text-align:justify;text-align-last:center;letter-spacing:.3px}
.hero .ctas{position:absolute;left:275px;top:173px;display:flex;gap:24px}
.btn{display:inline-block;background:var(--green);color:var(--ink);text-decoration:none}
.hero .btn{width:90px;height:29px;line-height:29px;text-align:center;font-family:"Asap Condensed",sans-serif;font-size:15px}

.feature{position:absolute;left:0;width:754px}
.feature h2{font-size:17.5px;font-weight:500;color:var(--ink)}
.feature h3{font-size:11.5px;font-weight:500;margin-top:12px}
.feature p{font-size:7.2px;line-height:14px;color:var(--body);text-align:justify;margin-top:13px}
.feature .btn{font-size:10px;color:var(--white);padding:5px 10px;margin-top:14px;font-weight:500}

.community{top:444px;height:238px;background:linear-gradient(100deg,#e9e9e9 0%,#d8d8d8 100%)}
.community .photo{position:absolute;left:0;top:0;width:330px;height:238px;background:radial-gradient(ellipse at 45% 55%,#6d6a64 0%,#8e8a82 40%,#bdb8ae 75%,#e0dcd4 100%)}
.community .copy{position:absolute;left:334px;top:40px;width:350px}
.community h3{word-spacing:3px}

.parents{top:682px;height:260px;background:var(--white)}
.parents .photo{position:absolute;left:30px;top:14px;width:260px;height:246px;background:radial-gradient(ellipse at 45% 50%,#d9b49a 0%,#e8d5c6 45%,#f6f1ec 80%,#ffffff 100%)}
.parents .copy{position:absolute;left:337px;top:42px;width:346px}
.parents h3{font-size:12.5px;margin-top:13px}

.students{top:942px;height:222px;background:var(--soft);text-align:center}
.students h2{margin-top:37px}
.students h3{font-size:12.5px;margin-top:9px}
.students p{width:510px;margin:13px auto 0;text-align:center;color:var(--muted)}

.footer{position:absolute;left:0;top:1164px;width:754px;height:36px;background:var(--black);color:var(--white);font-size:7.2px}
.footer .links{position:absolute;left:68px;top:14px}
.footer .legal{position:absolute;right:110px;top:14px}
.footer .code{position:absolute;right:30px;top:14px}
</style>
</head>
<body>
<div class="page">

  <div class="topbar">
    <div class="contact">
      <span>
        <svg width="8" height="8" viewBox="0 0 8 8"><rect x="0" y="0" width="8" height="8" rx="1.5" fill="#fff"/><path d="M2.2 1.8c.4 1.8 1.6 3.3 3.8 4.2l.6-.9-1-.6-.5.5c-.8-.4-1.4-1.1-1.8-1.9l.5-.5-.6-1z" fill="#0b0b0b"/></svg>
        (555) 014-2273
      </span>
      <span>
        <svg width="9" height="7" viewBox="0 0 9 7"><rect width="9" height="7" rx="1" fill="#fff"/><path d="M.5 .8 4.5 4 8.5 .8" fill="none" stroke="#0b0b0b" stroke-width=".8"/></svg>
        questions@HandwiseLessons.example
      </span>
    </div>
    <div class="social"><i></i><i></i><i></i></div>
  </div>

  <header class="header">
    <div class="brand"><span class="mark"></span><span class="name">Handwise Lessons</span></div>
    <div class="tagline">How To Learn ASL Through Video Lessons Online</div>
    <form class="login">
      <div class="field">User Name</div>
      <div class="field">Password</div>
      <div class="actions"><span class="forgot">Forgot Password</span><span class="signin">Sign In</span></div>
    </form>
  </header>

  <nav class="nav">
    <a class="active" href="#">Home</a>
    <a href="#">How it Works</a>
    <a href="#">Gift Certificates</a>
    <a href="#">Try it Free</a>
    <a href="#">Buy Now</a>
    <a href="#">Contact Us</a>
    <a href="#">Group Rate Form</a>
    <a href="#">Teacher's Guide</a>
  </nav>

  <section class="hero">
    <div class="photo" role="img" aria-label="Classroom of children raising their hands toward a teacher at the front"></div>
    <p class="lead">Handwise Lessons has the following free articles available about American sign language, which contain some great information, and some of the most commonly asked questions.</p>
    <div class="ctas"><a class="btn" href="#">Tutor</a><a class="btn" href="#">Free Trial</a></div>
  </section>

  <section class="feature community">
    <div class="photo" role="img" aria-label="Diverse group of people in a circle joining hands at the centre, seen from above"></div>
    <div class="copy">
      <h2>Learning Community</h2>
      <h3>Your Community Benefits When You Learn Sign Language</h3>
      <p>Every person in every walk of life has the need to know some sign language, even if you are not going to use that skill on a daily basis. For example, doctors, nurses, teachers, law enforcement, retail workers, and government employees are constantly frustrated with their inability to communicate with those who cannot hear because of their lack in ability to use sign language</p>
      <a class="btn" href="#">Read More</a>
    </div>
  </section>

  <section class="feature parents">
    <div class="photo" role="img" aria-label="Smiling family with a young daughter riding on her father's shoulders"></div>
    <div class="copy">
      <h2>Hearing Parents of Deaf Children</h2>
      <h3>Parents Benefit from Online Sign Language Classes</h3>
      <p>This comprehensive website, produced using American Sign Language, is designed to encourage parents of a deaf child to learn their language.</p>
      <p>Statistically, 85% of parents of deaf children do not know sign language, and it is our goal to change that percentage to a much lower number. Our online sign language classes allow you to learn at your own pace, and you can monitor your progress daily. If necessary, go back and review the lessons that you are not comfortable with before moving on.</p>
      <a class="btn" href="#">Read More</a>
    </div>
  </section>

  <section class="feature students">
    <h2>Deaf and Hard of Hearing Students</h2>
    <h3>Sign Language Skills Boost Student Confidence</h3>
    <p>The greatest accomplishment you can give yourself is the gift of learning. Knowledge provides you with the tools to be a better citizen and a more productive individual. This comprehensive website is designed to help you with that task of learning. You will improve your self-confidence and self-esteem while learning at your own pace.</p>
    <p>Daily, you will realize a dramatic improvement with reading comprehension, and in your sign language skills. You will also learn more about deaf culture by taking advantage of this completely user-friendly website produced in sign language. Watch, and participate, while improving on both your vocabulary and receptive abilities.</p>
  </section>

  <footer class="footer">
    <div class="links">Contact Us | Our Mission | Terms &amp; Conditions</div>
    <div class="legal">HandwiseLessons ©2017 All Rights Reserved | 1485181903.6238s</div>
    <div class="code">C12</div>
  </footer>

</div>
</body>
</html>
```